SKYVANTEX (drone photo and video) and Photogrammetry Services (mapping and 3D modeling)

We need a business card design for a SKYVANTEX. Our businesses provides (drone) Aerial Photo and Video Captures. However we also provide Photogrammetry (which is 3D modeling and mapping). We greatly value unique points of view taken of landscapes and subjects with aerial photography and videography. 3D modeling and mapping is the other area of focus and have an incredibly broad scope of applications and imaginative creativity.

Target Market(s)

Based out of Northern Virginia and serving the greater Virginia and Maryland areas

Industry/Entity Type

Drone Photo and video and Photogrammetry Services (mapping and 3D modeling)

Contact Information for Business Card

3D Models, Maps and Photo/Video Production name: Marcus Pettibone email: mqp@skyvantex.us website: skyvantex.us phone: 571-806-3394; please also include "Aerial Photo/Video and 3D Mapping/Modeling"

Requirements
Must have
• Please make this design vertical and double sided. The selection box is not letting me choose Double Sided but that is my wish. Incorporate uploaded LOGO and color scheme
Nice to have
• Preferably does not feel too crowded and balances not having an exaggerated amount of distracting detail
Should not have
• do not cram bullet points or text in long form

```html
<!DOCTYPE html>
<html lang="en">
<head>
<meta charset="utf-8">
<title>SKYVANTEX Business Card</title>
<link href="https://fonts.googleapis.com/css2?family=Poppins:wght@400;500;700&display=swap" rel="stylesheet">
<style>
  :root {
    --bg: #e9e9ea;
    --card-white: #ffffff;
    --ink: #1a1a1a;
    --ink-soft: #555555;
    --brand-red: #ee2a2e;
    --brand-orange: #f7941d;
    --brand-amber: #f9a825;
    --ghost-grey: #ececec;
    --rule-grey: #8a8a8a;
  }
  html, body {
    margin: 0;
    padding: 0;
    width: 1200px;
    height: 1108px;
    overflow: hidden;
    background: var(--bg);
  }
  .canvas {
    position: relative;
    width: 1200px;
    height: 1108px;
    display: flex;
    justify-content: center;
    align-items: center;
    gap: 80px;
  }
  .card {
    position: relative;
    width: 400px;
    height: 700px;
    border-radius: 26px;
    overflow: hidden;
    box-shadow: 0 10px 30px rgba(0,0,0,0.18);
  }

  /* Front */
  .card-front {
    background: var(--card-white);
    font-family: 'Poppins', sans-serif;
  }
  .drone-art {
    position: absolute;
    left: 20px;
    top: 330px;
    width: 360px;
    height: 190px;
    border-radius: 60px;
    background: radial-gradient(ellipse at 50% 45%, var(--ghost-grey) 0%, rgba(236,236,236,0.55) 55%, rgba(255,255,255,0) 100%);
  }
  .brand {
    position: absolute;
    top: 70px;
    left: 0;
    right: 0;
    display: flex;
    flex-direction: column;
    align-items: center;
  }
  .brand-dot {
    width: 112px;
    height: 112px;
    border-radius: 50%;
    background: var(--brand-orange);
    margin-bottom: 20px;
  }
  .brand-name {
    font-weight: 700;
    font-size: 48px;
    letter-spacing: 1px;
    color: var(--brand-red);
    line-height: 1;
  }
  .person {
    position: absolute;
    top: 278px;
    left: 0;
    right: 0;
    text-align: center;
  }
  .person-name {
    margin: 0;
    font-weight: 500;
    font-size: 20px;
    line-height: 1.3;
    color: var(--ink);
  }
  .person-tagline {
    margin: 4px 0 0;
    font-weight: 400;
    font-size: 13px;
    line-height: 1.3;
    color: var(--ink-soft);
  }
  .contact {
    position: absolute;
    left: 0;
    right: 0;
    top: 500px;
    text-align: center;
    color: var(--ink);
  }
  .contact-icons {
    display: flex;
    align-items: center;
    justify-content: center;
    gap: 10px;
    margin-bottom: 16px;
  }
  .contact-rule {
    width: 70px;
    height: 1px;
    background: var(--rule-grey);
  }
  .icon-tile {
    width: 34px;
    height: 34px;
    border-radius: 6px;
    background: linear-gradient(160deg, var(--brand-orange), var(--brand-red));
    display: flex;
    align-items: center;
    justify-content: center;
  }
  .contact-line {
    font-size: 21px;
    line-height: 1.4;
    margin: 0;
  }

  /* Back */
  .card-back {
    background: linear-gradient(180deg, var(--brand-amber) 0%, var(--brand-orange) 35%, var(--brand-red) 100%);
  }
  .back-texture {
    position: absolute;
    inset: 0;
    background: linear-gradient(180deg, rgba(255,255,255,0.06), rgba(0,0,0,0.04));
  }
  .back-mark {
    position: absolute;
    right: 54px;
    bottom: 150px;
    font-family: 'Poppins', sans-serif;
    font-weight: 700;
    font-size: 16px;
    letter-spacing: 1px;
    color: var(--card-white);
  }
</style>
</head>
<body>
<main class="canvas">
  <section class="card card-front" aria-label="Card front">
    <div class="drone-art" role="img" aria-label="Faint grey silhouette of a quadcopter drone"></div>
    <div class="brand">
      <div class="brand-dot"></div>
      <div class="brand-name">SKYVANTEX</div>
    </div>
    <div class="person">
      <p class="person-name">Marcus Pettibone</p>
      <p class="person-tagline">Aerial Photo/Video and 3D Mapping/Modeling</p>
    </div>
    <div class="contact">
      <div class="contact-icons">
        <span class="contact-rule"></span>
        <span class="icon-tile" aria-label="Phone">
          <svg width="20" height="20" viewBox="0 0 24 24"><path fill="#fff" d="M6.6 10.8a15.1 15.1 0 0 0 6.6 6.6l2.2-2.2c.3-.3.7-.4 1-.2 1.1.4 2.3.6 3.6.6.6 0 1 .4 1 1V20c0 .6-.4 1-1 1A17 17 0 0 1 3 4c0-.6.4-1 1-1h3.5c.6 0 1 .4 1 1 0 1.3.2 2.5.6 3.6.1.3 0 .7-.2 1z"/></svg>
        </span>
        <span class="icon-tile" aria-label="Email">
          <svg width="20" height="20" viewBox="0 0 24 24"><rect x="3" y="5" width="18" height="14" rx="1.5" fill="none" stroke="#fff" stroke-width="2"/><path d="M3 6l9 7 9-7" fill="none" stroke="#fff" stroke-width="2"/></svg>
        </span>
        <span class="icon-tile" aria-label="Website">
          <svg width="20" height="20" viewBox="0 0 24 24"><circle cx="12" cy="12" r="9" fill="none" stroke="#fff" stroke-width="2"/><path d="M3 12h18M12 3c3 3 3 15 0 18M12 3c-3 3-3 15 0 18" fill="none" stroke="#fff" stroke-width="1.5"/></svg>
        </span>
        <span class="contact-rule"></span>
      </div>
      <p class="contact-line">571-806-3394</p>
      <p class="contact-line">mqp@skyvantex.us</p>
      <p class="contact-line">skyvantex.us</p>
    </div>
  </section>

  <section class="card card-back" aria-label="Card back">
    <div class="back-texture" role="img" aria-label="Subtle embossed repeating brand pattern on orange-to-red gradient"></div>
    <div class="back-mark">SKYVANTEX</div>
  </section>
</main>
</body>
</html>
```